Mobile Recording Studio needs business cards

Open to seeing a creative design, but I want to emphasis my logo and minimize the name/title and company information. Possible a fully black background on card.

My company is a mobile sound recording studio. ok to include a my trailer (actual or cartoon) on the card. My initial thought is more straight forward, but a good design will win me over.

SPECS:
CMYK color mode
High (300ppi) raster effect.
cover bleed area
please deliver: Illustrator file with layers and a pdf at completion.

Name and info for the business card:

Dallin Perry
ADR Mixer

email: Dallin@MixVault.com

address:
248 - 5170 East Hollister
Vancouver, BC V5R 2J4

phone:
604.518.2093 office

website:
www.MixVault.com

FB: @MixVault

photos: @TheMixVault

Industry/Entity Type

Television Production

Contact Information for Business Card

Dallin Perry
ADR Mixer

email: Dallin@MixVault.com

address:
248 - 5170 East Hollister
Vancouver, BC V5R 2J4

phone:
604.518.2093 office

website:
www.MixVault.com

FB: @MixVault

photos: @TheMixVault

Colors

Designer to choose colors to be used in the design.

Requirements
Must have
• emphasis my logo and minimize the name/title and company information.
• SPECS:
• CMYK color mode
• High (300ppi) raster effect.
• cover bleed area
• please deliver: Illustrator file with layers and a pdf at completion.
Nice to have
• maybe include the following:
• all black background or black theme
• my work trailer (actual or cartoon) refer to photos: @TheMixVault

```html
<!DOCTYPE html>
<html lang="en">
<head>
<meta charset="utf-8">
<title>MixVault Business Card</title>
<link rel="stylesheet" href="https://fonts.googleapis.com/css2?family=Lato:wght@400;700&display=swap">
<style>
  :root {
    --backdrop: #8a8a8a;
    --card: #161616;
    --card-edge: #222222;
    --silver: #d6d6d6;
    --silver-soft: #bdbdbd;
    --rule: #a9a9a9;
  }
  html, body {
    margin: 0;
    width: 1200px;
    height: 912px;
    overflow: hidden;
    background: var(--backdrop);
  }
  .stage {
    position: relative;
    width: 1200px;
    height: 912px;
    display: flex;
    align-items: center;
    justify-content: center;
  }
  .card {
    position: relative;
    width: 1000px;
    height: 572px;
    background: linear-gradient(160deg, #1e1e1e 0%, var(--card) 55%, #101010 100%);
    border: 1px solid var(--card-edge);
    font-family: "Lato", sans-serif;
    color: var(--silver);
    box-sizing: border-box;
  }
  .brand {
    position: absolute;
    left: 0;
    right: 0;
    top: 70px;
    text-align: center;
    font-family: "Lato", sans-serif;
    font-weight: 700;
    font-size: 150px;
    line-height: 1;
    letter-spacing: -2px;
    color: var(--silver);
    margin: 0;
  }
  .rule {
    position: absolute;
    height: 2px;
    background: var(--rule);
  }
  .rule--upper { left: 300px; right: 60px; top: 262px; }
  .rule--info { left: 60px; width: 560px; top: 410px; }
  .holder {
    position: absolute;
    left: 330px;
    top: 348px;
    margin: 0;
    font-size: 30px;
    font-weight: 400;
    color: var(--silver);
    white-space: nowrap;
  }
  .holder .role {
    font-size: 18px;
    color: var(--silver-soft);
    margin-left: 6px;
  }
  .contact {
    position: absolute;
    left: 60px;
    top: 430px;
    margin: 0;
    font-size: 20px;
    line-height: 34px;
    color: var(--silver);
    white-space: nowrap;
  }
  .contact .line { display: block; }
  .contact .note { font-size: 16px; color: var(--silver-soft); }
</style>
</head>
<body>
  <main class="stage">
    <article class="card">
      <h1 class="brand">MixVault</h1>
      <div class="rule rule--upper"></div>

      <p class="holder">Dallin Perry <span class="role">/ ADR Mixer</span></p>
      <div class="rule rule--info"></div>

      <p class="contact">
        <span class="line">248 - 5170 East Hollister, Vancouver, BC V5R 2J4 &bull; 604.518.2093 <span class="note">(office)</span></span>
        <span class="line">www.MixVault.com &bull; @MixVault <span class="note">(page)</span> &bull; @TheMixVault <span class="note">(photos)</span></span>
      </p>
    </article>
  </main>
</body>
</html>
```